Web Design Front Page Only for Organic Skincare

We have been in business for nearly 20 years. We are run by all females and sell anything from aromatherapy, skincare and pharmacy types products to health food shops and pharmacy. We are looking for an attractive and colourful but simple front web page design for our wholesale customers to look at. We want our customers to start using our website to find information rather than ringing us. So we want it to be attractive to our buyers who are young and funky.
Updates

To give you an idea of the products we sell to pharmacy and health food shops also beauty shops and hair salons.  We mainly deal with organic body and skincare, aromatherapy oils and body products, but also do some simple pharmacy products such as bandages and pill boxes, finger splits, walking frames and wheelchairs.  We are only looking for the front page of the website.  The back-end will be done in-house.  We currently do not have a logo designed so I am thinking that once we have done the website design we can build a logo from it.  I like bright colours and want something that is inviting to further discover that we do many different types of products.

Target Market(s)

young girls who are our retail buyers

Industry/Entity Type

Pharmacy

Requirements
Must have
• A section which says

Customer Log in
Should not have
• don't worry about too much writing or tabs. We will insert these later. Just come up with design image.

```html
<!DOCTYPE html>
<html lang="en">
<head>
<meta charset="utf-8">
<title>Verdalia Healthcare — Home</title>
<link href="https://fonts.googleapis.com/css2?family=Open+Sans:ital,wght@0,300;0,400;0,600;1,400&family=PT+Sans:wght@400;700&display=swap" rel="stylesheet">
<style>
:root{
  --orange:#f7a21b;
  --orange-dark:#e8860c;
  --orange-pale:#fde9b8;
  --cream:#fff8e4;
  --green:#7e9f2a;
  --green-dark:#5f7c18;
  --green-light:#a1bf45;
  --brand:#a56c22;
  --text:#555555;
  --text-soft:#8a7d6e;
  --line:#e3e3e3;
  --panel:#fbfbfb;
  --white:#ffffff;
}
*{box-sizing:border-box;margin:0;padding:0}
html,body{width:921px;height:1200px;overflow:hidden}
body{position:relative;background:var(--white);font-family:"Open Sans",Arial,sans-serif;color:var(--text)}
.abs{position:absolute}

/* header & hero */
.hero-bg{left:0;top:0;width:921px;height:428px;
  background:linear-gradient(180deg,#ffb326 0%,#ffc74a 18%,#ffe08f 55%,#fff5dc 88%,#ffffff 100%)}
.hero-bg::before{content:"";position:absolute;left:0;top:0;width:921px;height:85px;
  background:linear-gradient(90deg,rgba(255,150,0,.55),rgba(255,200,80,.2) 50%,rgba(255,150,0,.45))}
.util-btn{top:0;height:22px;border-radius:0 0 3px 3px;
  background:linear-gradient(#ffc04a,#f39a12);color:#5b3a0b;font-size:10px;font-weight:600;
  text-align:center;line-height:21px;box-shadow:0 1px 2px rgba(120,60,0,.35)}
.logo{left:116px;top:24px;font-family:"PT Sans",sans-serif;font-size:34px;color:var(--brand);letter-spacing:.3px}
.search{left:668px;top:53px;width:111px;height:17px;background:var(--cream);border:1px solid #f1c46b;
  font-size:9px;font-style:italic;color:#e0b160;padding-left:6px;line-height:15px}
.search-go{left:779px;top:53px;width:29px;height:17px;background:linear-gradient(#ffb93a,#ef8d0a);
  color:var(--white);font-size:9px;font-weight:700;text-align:center;line-height:17px}
.tab{top:82px;height:25px;border-radius:3px 3px 0 0;background:linear-gradient(#ffc24d,#f59c14);
  color:#5d3b0c;font-size:11px;text-align:center;line-height:24px;box-shadow:0 1px 3px rgba(150,80,0,.35)}
.tab.active{background:linear-gradient(#ffffff,#e4e4e4);color:#333}
.subnav{top:130px;font-size:8.5px;font-style:italic;color:#f0bf7c;letter-spacing:.4px}
.hero-photo{left:0;top:143px;width:430px;height:282px;
  background:radial-gradient(ellipse at 55% 45%,#f3d3b6 0%,#eec39c 35%,#f7dc97 70%,rgba(255,236,180,0) 100%)}
.hero-watermark{left:112px;top:202px;font-family:"PT Sans",sans-serif;font-size:66px;color:rgba(255,255,255,.32);white-space:nowrap}
.headline{left:446px;top:252px;font-size:37px;font-weight:300;color:#555;letter-spacing:-.5px}
.headline span{color:var(--orange)}
.hero-copy{left:446px;width:362px;font-size:10px;line-height:12px;color:var(--text-soft)}
.btn-orange{background:linear-gradient(#ffb433,#f0860a);color:var(--white);border-radius:3px;
  font-size:9.5px;font-weight:600;text-align:center;box-shadow:0 1px 2px rgba(0,0,0,.2)}

/* panels */
.panel{background:var(--panel);border:1px solid #eeeeee;border-radius:3px;box-shadow:0 3px 5px rgba(0,0,0,.05)}
.ribbon{height:28px;background:linear-gradient(#93b43a,#6f9020);color:var(--white);
  font-family:"PT Sans",sans-serif;font-size:16px;line-height:27px;padding-left:18px;border-radius:0 3px 3px 0;
  box-shadow:0 2px 3px rgba(0,0,0,.2)}
.ribbon::before{content:"";position:absolute;left:0;bottom:-6px;border-top:6px solid var(--green-dark);border-left:11px solid transparent}
.ribbon small{font-size:12px}
.product-list{left:120px;top:484px;width:164px;list-style:none}
.product-list li{height:22.3px;border-bottom:1px solid var(--line);font-size:10px;line-height:21px;padding-left:31px;position:relative;color:#555}
.product-list li:last-child{border-bottom:none}
.product-list li::before{content:"";position:absolute;left:8px;top:5px;width:11px;height:11px;border-radius:50%;
  background:radial-gradient(circle,#666 0 2px,#fff 2.5px 3.5px,#888 4px)}
.quote-icon{width:19px;height:19px;border-radius:50%;background:#6d6d6d}
.testimonial{left:156px;width:130px;font-size:9.5px;line-height:11px;color:#555}
.author{font-size:9.5px;font-style:italic;color:var(--green);text-align:right;width:60px}
.rule{height:1px;background:var(--line)}
.newsletter-copy{left:128px;top:944px;width:150px;font-size:9.5px;line-height:11px}
.email{left:128px;top:1003px;width:99px;height:21px;border:1px solid #ddd;border-radius:3px 0 0 3px;
  background:linear-gradient(#ffffff,#e8e8e8);font-size:9.5px;color:#777;padding-left:7px;line-height:20px}
.subscribe{left:226px;top:1003px;width:63px;height:21px;border-radius:0 3px 3px 0;line-height:21px;font-size:10px}

.main-copy{font-size:9.8px;line-height:10.9px;color:#555}
.thumb{width:81px;height:60px}
.thumb-label{position:absolute;left:0;bottom:0;width:100%;height:13px;background:rgba(60,60,60,.6);
  color:var(--white);font-size:9px;line-height:13px;padding-left:4px}
.more{width:41px;height:18px;line-height:18px;font-size:9px}

.tips-banner{left:330px;top:968px;width:478px;height:69px;background:linear-gradient(90deg,#f4f7ea,#ffffff 40%,#ffffff 70%,#f6f6f6);
  border:1px solid #eeeeee}
.sticky{left:672px;top:966px;width:50px;height:46px;background:#f7e23a;transform:rotate(-8deg);
  box-shadow:1px 2px 3px rgba(0,0,0,.25);font-size:10px;font-style:italic;color:#4a4a2a;text-align:center;line-height:13px;padding-top:8px}

.footer-links{left:119px;top:1079px;font-size:9px;color:#444}
.copyright{left:119px;top:1094px;font-size:8px;color:#666}
.follow{left:649px;top:1092px;font-size:9px;color:#444}
.social{top:1089px;width:17px;height:17px;border-radius:2px;background:#333}
.footer-band{left:0;top:1120px;width:921px;height:80px;
  background:linear-gradient(180deg,#ffffff 0%,#ffe7a3 40%,#ffc23f 100%)}
.footer-watermark{left:232px;top:1135px;font-family:"PT Sans",sans-serif;font-size:44px;color:rgba(255,255,255,.55);white-space:nowrap}
</style>
</head>
<body>

<header>
  <div class="abs hero-bg"></div>
  <a class="abs util-btn" style="left:621px;width:53px">Home</a>
  <a class="abs util-btn" style="left:685px;width:59px">Log in</a>
  <a class="abs util-btn" style="left:754px;width:54px">Sitemap</a>
  <div class="abs logo">Verdalia Healthcare</div>
  <div class="abs search">--search--</div>
  <div class="abs search-go">GO!</div>

  <nav>
    <a class="abs tab active" style="left:120px;width:46px">Home</a>
    <a class="abs tab" style="left:180px;width:63px">about us</a>
    <a class="abs tab" style="left:257px;width:75px">healthfood</a>
    <a class="abs tab" style="left:345px;width:68px">pharmacy</a>
    <a class="abs tab" style="left:426px;width:61px">skincare</a>
    <a class="abs tab" style="left:500px;width:68px">contact us</a>
  </nav>
  <div class="abs subnav" style="left:119px">CONTACT US</div>
  <div class="abs subnav" style="left:197px">ABOUT US</div>
  <div class="abs subnav" style="left:269px">HEALTH FOOD</div>
  <div class="abs subnav" style="left:349px">PHARMACY</div>
  <div class="abs subnav" style="left:411px">SUPERMARKET</div>
  <div class="abs subnav" style="left:489px">BEAUTY</div>
</header>

<section class="hero">
  <div class="abs hero-watermark">Verdalia Healthcare</div>
  <div class="abs hero-photo" role="img" aria-label="Photo of a woman resting with a yellow calla lily"></div>
  <h1 class="abs headline">the <span>happiness</span> of life</h1>
  <p class="abs hero-copy" style="top:311px">Typi non habent claritatem insitam; est usus legentis in iis qui facit eorum claritatem. Investigationes demonstraverunt lectores legere me lius quod ii legunt saepius. Claritas est etiam processus dynamicus.</p>
  <p class="abs hero-copy" style="top:358px">Duis autem vel eum iriure dolor in hendrerit in vulputate velit esse molestie consequat, vel illum dolore eu feugiat nulla facilisis at vero eros et accumsan et iusto odio dignissim qui blandit praesent .</p>
  <a class="abs btn-orange" style="left:748px;top:406px;width:59px;height:20px;line-height:20px">view more</a>
</section>

<aside>
  <div class="abs panel" style="left:120px;top:442px;width:180px;height:224px"></div>
  <h2 class="abs ribbon" style="left:106px;top:447px;width:183px;font-weight:400">Products</h2>
  <ul class="abs product-list">
    <li>Aromatherapy Oils</li><li>Pharmacy</li><li>Body</li><li>Health Food</li>
    <li>Pill boxes</li><li>Finger Splits</li><li>Walking Frames</li><li>Wheelchairs</li>
  </ul>

  <div class="abs panel" style="left:120px;top:682px;width:180px;height:201px"></div>
  <h2 class="abs ribbon" style="left:106px;top:688px;width:183px;font-weight:400">Our Testimonials</h2>
  <div class="abs quote-icon" style="left:129px;top:726px"></div>
  <p class="abs testimonial" style="top:728px">Vel illum dolore eu feugiatn ulla facilisis at vero eros et accumsan.</p>
  <div class="abs author" style="left:230px;top:757px">Aish</div>
  <div class="abs rule" style="left:129px;top:772px;width:160px"></div>
  <div class="abs quote-icon" style="left:129px;top:781px"></div>
  <p class="abs testimonial" style="top:783px">Aillum dolore eu feugiat nulla facilisis at vero eros et accu msan.</p>
  <div class="abs author" style="left:230px;top:818px">Jenny</div>
  <div class="abs rule" style="left:129px;top:832px;width:160px"></div>
  <div class="abs quote-icon" style="left:129px;top:840px"></div>
  <p class="abs testimonial" style="top:842px">Elillum dolore eu feugiat nulla facilisis.</p>
  <div class="abs author" style="left:230px;top:864px">yashmin</div>

  <div class="abs panel" style="left:120px;top:902px;width:180px;height:135px"></div>
  <h2 class="abs ribbon" style="left:106px;top:907px;width:183px;font-weight:400">Newsletter</h2>
  <p class="abs newsletter-copy">Sign up for our newsletter and receive the latest Verdalia Healthcare news in your email inbox!</p>
  <div class="abs email">Email</div>
  <a class="abs btn-orange subscribe">Subscribe</a>
</aside>

<main>
  <div class="abs panel" style="left:330px;top:442px;width:478px;height:162px"></div>
  <h2 class="abs ribbon" style="left:317px;top:447px;width:256px;font-weight:400"><small>Welcome to</small> Verdalia Healthcare</h2>
  <div class="abs" style="left:341px;top:485px;width:97px;height:109px;border:1px solid #ddd;background:linear-gradient(90deg,#6f9a4a,#c9d6b4 40%,#e8d2bf 60%,#7aa353)" role="img" aria-label="Photo of a woman among aloe vera leaves"></div>
  <div class="abs main-copy" style="left:451px;top:485px;width:340px">
    <p>Non habent claritatem insitam est usus legentis in iis qui facit eorum claritatem. Investigationes demonstraverunt lectores legere me lius quod ii legunt saepius. Claritas est etiam processus dynamicus. Conse ctetuerad dipiscing elit, sed diam nonummy nibh euismod tincidunt Ut laoreetdolac ore magna aliquam erat volutpat.</p>
    <p style="margin-top:11px">Ut wisi enim ad minim veniam, quis nostrud exerci tation ullamcorpersu scipit lobortis nisl ut aliquip ex ea commodo consequat. Duis autem vel eum iriure dolor in hendrerit in vulputate.</p>
  </div>

  <div class="abs panel" style="left:330px;top:619px;width:478px;height:333px"></div>
  <h2 class="abs ribbon" style="left:317px;top:624px;width:155px;font-weight:400">Featured Products</h2>

  <div class="abs thumb" style="left:341px;top:663px;background:linear-gradient(135deg,#c9a31a,#f2d467 50%,#7c8a3a)" role="img" aria-label="Photo of aromatherapy oil bottles"><span class="thumb-label">Dynamicus</span></div>
  <p class="abs main-copy" style="left:435px;top:662px;width:365px">Habent claritatem insitam est usus legentis in iis qui facit eorum clarittem.Investigationes demonstraverunt lectores legere me lius quod ii legunt sae pius. Claritas est etiam processus dynamicus. esse molestie consequat, vel illum dolore eu feugiat nulla facilisis.</p>
  <a class="abs btn-orange more" style="left:756px;top:705px">› more</a>
  <div class="abs rule" style="left:340px;top:732px;width:458px"></div>

  <div class="abs thumb" style="left:341px;top:735px;background:linear-gradient(160deg,#ffffff,#f1dcc6 55%,#d49a5a)" role="img" aria-label="Photo of a hand with an oil dropper"><span class="thumb-label">Claritatem</span></div>
  <p class="abs main-copy" style="left:435px;top:734px;width:365px">Abent claritatem insitam est usus legentis in iis qui facit eorum claritatem.Inve stigationes demonstraverunt.Ctores legere me lius quod ii legunt saepius. Claritas est etiam processus dynamicus.Autem vel eum.</p>
  <a class="abs btn-orange more" style="left:756px;top:777px">› more</a>
  <div class="abs rule" style="left:340px;top:804px;width:458px"></div>

  <div class="abs thumb" style="left:341px;top:807px;background:linear-gradient(135deg,#5f9a2e,#cfe5b2 50%,#f3f6f1)" role="img" aria-label="Photo of fresh green leaves"><span class="thumb-label">Autemvel</span></div>
  <p class="abs main-copy" style="left:435px;top:806px;width:365px">Claritatem insitam est usus legentis in iis qui facit eorum claritatem. Investigationes demonstraverunt legere me lius quod ii legunt saepius. Claritas estetia processus dynamicus.Autem vel eum.</p>
  <a class="abs btn-orange more" style="left:756px;top:849px">› more</a>
  <div class="abs rule" style="left:340px;top:876px;width:458px"></div>

  <div class="abs thumb" style="left:341px;top:879px;background:linear-gradient(135deg,#5f9a2e,#cfe5b2 50%,#f3f6f1)" role="img" aria-label="Photo of fresh green leaves"><span class="thumb-label">Autemvel</span></div>
  <p class="abs main-copy" style="left:435px;top:879px;width:365px">Insitam est usus legentis in iis qui facit eorum claritatem. Investiga tiones de onstraverunt legere me lius quod ii legunt saepius. Claritas est etiam process dynamicus.Autem vel eum.</p>

  <div class="abs tips-banner"></div>
  <div class="abs" style="left:331px;top:969px;width:125px;height:67px;background:linear-gradient(90deg,#e9cdb3,#9cc25a 60%,rgba(255,255,255,0))" role="img" aria-label="Photo of a woman with a large green leaf"></div>
  <div class="abs" style="left:468px;top:982px;font-size:13px;color:#666">Tips for your</div>
  <div class="abs" style="left:467px;top:995px;font-size:23px;color:var(--green-light);letter-spacing:-.2px">beauty and health</div>
  <div class="abs" style="left:715px;top:969px;width:92px;height:67px;background:linear-gradient(90deg,rgba(255,255,255,0),#f2dccb 45%,#f6f6f6)" role="img" aria-label="Photo of a smiling woman applying cream"></div>
  <div class="abs sticky">Today<br>tips</div>
</main>

<footer>
  <div class="abs rule" style="left:0;top:1062px;width:921px;background:#ececec"></div>
  <nav class="abs footer-links">Home &nbsp;| &nbsp;about us &nbsp;| &nbsp;healthcare &nbsp;| &nbsp;products &nbsp;| &nbsp;skincare &nbsp;| &nbsp;contact us</nav>
  <div class="abs copyright">copyright(C)2012 verdaliahealthcare.com All Right Reserved</div>
  <div class="abs follow">Follow &amp; Share us:</div>
  <div class="abs social" style="left:734px" aria-label="Social link"></div>
  <div class="abs social" style="left:753px" aria-label="Social link"></div>
  <div class="abs social" style="left:772px" aria-label="Social link"></div>
  <div class="abs social" style="left:791px" aria-label="Feed link"></div>
  <div class="abs footer-band"></div>
  <div class="abs footer-watermark">Verdalia Healthcare</div>
</footer>

</body>
</html>
```